Design a Website Mockup for a Mobile Coffee Business

Hey all,
We're looking for a fresh, BRIGHT, unique website design. The design only has to be for the homepage at this stage.
We love the simplicity and crispness of these websites:
http://www.tidalroast.com.au
http://quietlantern.com/
http://solbrixhub.com/
Our color pallet is Orange and brown, however, our logo works with Black and White.
We'd like the design to be compatible with Bootstrap and Wordpress.
If you are using an existing Wordpress theme as your inspiration, PLEASE include the theme name.
The Design must have these elements:
* A Contact Phone number: 1300 482 917
* 3 Stand out Points:
"Our Difference"
---1. We cater to your theme.
---- We can provide a cart that blends seamlessly into your decor or theme. Whether it's a woodern, rustic or bright red, we have a cart and the coffee machines to suit every occasion
--- 2. We Go the extra mile
------ We love what we do and provide above and beyond service and hospitality.
--- 3. We listen to your needs
------ No two carts are the same as we understand that your event, theme or occasion are unique and special. We'd love to provide you with a coffee experience that excites and delights.
* A footer section which presents an instagram feed.
----
We have a number of pictures attached below which you can use throughout the design. They have been made smaller - it is OK if you blow these pictures for your design (and cause pixelation)
----
For any further questions, please ask.
Thank you.

```html
<!DOCTYPE html>
<html lang="en">
<head>
<meta charset="utf-8">
<title>the bean cart — Home</title>
<link rel="stylesheet" href="https://fonts.googleapis.com/css2?family=Arimo:wght@400;700&family=Roboto+Condensed:ital,wght@0,300;0,400;1,400&family=Lora:ital@1&display=swap">
<style>
  :root {
    --orange: #ee8a1a;
    --orange-deep: #e07b10;
    --brown: #3a2a1c;
    --ink: #333333;
    --muted: #666666;
    --soft: #8a8a8a;
    --line: #e4e4e4;
    --hero-bg: #e8e8e3;
    --white: #ffffff;
  }
  * { box-sizing: border-box; margin: 0; padding: 0; }
  html, body { width: 962px; height: 1200px; overflow: hidden; background: var(--white); }
  body { position: relative; font-family: "Arimo", Arial, sans-serif; color: var(--ink); }

  .site-header { position: absolute; left: 0; top: 0; width: 962px; height: 84px; border-bottom: 1px solid var(--line); }
  .brand {
    position: absolute; left: 452px; top: 12px; width: 57px; height: 62px;
    background: var(--orange); border-radius: 6px;
    display: flex; align-items: center; justify-content: center; text-align: center;
    font-family: "Arimo", Arial, sans-serif; font-weight: 700; font-size: 11px; line-height: 12px;
    color: var(--brown); padding: 4px;
  }
  .cart { position: absolute; left: 702px; top: 15px; font-size: 8.5px; color: var(--ink); display: flex; align-items: center; gap: 4px; }
  .cart strong { font-weight: 700; }
  .search {
    position: absolute; left: 768px; top: 11px; width: 123px; height: 20px;
    border: 1px solid #cfcfcf; font-size: 8px; color: var(--soft);
    padding: 5px 7px; display: flex; justify-content: space-between; align-items: center;
  }

  .main-nav { position: absolute; left: 0; top: 86px; width: 962px; height: 35px; }
  .main-nav ul { position: absolute; left: 259px; top: 12px; display: flex; gap: 0; list-style: none; }
  .main-nav li { font-size: 9px; color: #555; text-transform: uppercase; margin-right: 24px; letter-spacing: .2px; }
  .main-nav li.active { color: var(--ink); border-bottom: 1px solid var(--orange); padding-bottom: 3px; }
  .nav-divider { position: absolute; left: 591px; top: 0; width: 1px; height: 35px; background: var(--line); }
  .call { position: absolute; left: 613px; top: 11px; font-size: 10px; color: var(--ink); }
  .call em { color: var(--orange); font-weight: 700; font-style: italic; margin-left: 3px; }

  .hero { position: absolute; left: 0; top: 121px; width: 962px; height: 326px; background: var(--hero-bg); text-align: center; }
  .hero-kicker { position: absolute; top: 76px; width: 100%; font-family: "Lora", Georgia, serif; font-style: italic; font-size: 10px; color: var(--ink); }
  .hero-title {
    position: absolute; top: 98px; width: 100%;
    font-family: "Roboto Condensed", "Arial Narrow", sans-serif; font-weight: 300;
    font-size: 25px; line-height: 31px; color: #5a5a58; text-transform: uppercase;
  }
  .hero-button {
    position: absolute; left: 404px; top: 185px; width: 155px; height: 29px;
    border: 2px solid var(--orange); font-size: 10px; font-weight: 700; color: var(--ink);
    display: flex; align-items: center; justify-content: center; text-transform: uppercase;
  }
  .hero-dots { position: absolute; left: 456px; top: 277px; display: flex; gap: 6px; }
  .hero-dots span { width: 8px; height: 8px; border-radius: 50%; border: 1px solid var(--orange); }
  .hero-dots span.on { background: var(--orange); }

  .section-title {
    position: absolute; width: 962px; text-align: center;
    font-family: "Roboto Condensed", "Arial Narrow", sans-serif; font-weight: 300;
    font-size: 15px; color: #666; text-transform: uppercase; letter-spacing: .3px;
  }
  .difference-title { top: 510px; }
  .points { position: absolute; left: 0; top: 568px; width: 962px; }
  .point { position: absolute; width: 232px; text-align: center; }
  .point svg { display: block; margin: 0 auto; }
  .point h3 { margin-top: 18px; font-size: 13px; font-weight: 400; color: var(--ink); }
  .point p { margin-top: 11px; font-size: 9.5px; line-height: 14px; color: var(--muted); }

  .rule { position: absolute; left: 98px; top: 762px; width: 765px; height: 1px; background: var(--line); }
  .carts-title { top: 823px; }

  .gallery { position: absolute; left: 12px; top: 871px; width: 941px; height: 321px; }
  .photo { position: absolute; }
  .photo.tall { left: 0; top: 0; width: 232px; height: 321px; background: linear-gradient(180deg, #b9cde0 0%, #cfcfcf 30%, #efefef 60%, #d9d6cf 100%); }
  .p1 { left: 235px; top: 0; width: 232px; height: 158px; background: linear-gradient(160deg, #4e4036, #8a6a48 55%, #c7a57a); }
  .p2 { left: 471px; top: 0; width: 232px; height: 158px; background: linear-gradient(160deg, #6f6a63, #9e9890 50%, #5f5a52); }
  .p3 { left: 706px; top: 0; width: 232px; height: 158px; background: linear-gradient(160deg, #4e4036, #8a6a48 55%, #c7a57a); }
  .p4 { left: 235px; top: 163px; width: 232px; height: 158px; background: linear-gradient(160deg, #4a4944, #7b7c72 50%, #3e3a32); }
  .p5 { left: 471px; top: 163px; width: 232px; height: 158px; background: linear-gradient(160deg, #6e5e4e, #a89a86 50%, #6b6154); }
  .p6 { left: 706px; top: 163px; width: 232px; height: 158px; background: linear-gradient(160deg, #4a4944, #7b7c72 50%, #3e3a32); }
</style>
</head>
<body>

<header class="site-header">
  <div class="brand">the bean cart</div>
  <div class="cart">
    <svg width="11" height="10" viewBox="0 0 11 10"><path d="M0 1h2l1.5 5h5.5l1.5-4H3" fill="none" stroke="#555" stroke-width="1"/><circle cx="4" cy="8.5" r="1" fill="#555"/><circle cx="8.5" cy="8.5" r="1" fill="#555"/></svg>
    Cart: <strong>$0.00</strong>
  </div>
  <div class="search">
    <span>Search for a product</span>
    <svg width="12" height="10" viewBox="0 0 12 10"><circle cx="4" cy="4" r="3" fill="none" stroke="#777" stroke-width="1.3"/><path d="M6.3 6.2l4.5 3.3" stroke="#777" stroke-width="1.6"/></svg>
  </div>
</header>

<nav class="main-nav">
  <ul>
    <li class="active">Home</li>
    <li>About</li>
    <li>Store</li>
    <li>Wholesale</li>
    <li>Blog</li>
    <li>Contact</li>
  </ul>
  <div class="nav-divider"></div>
  <div class="call">Call us: <em>1300 482 917</em></div>
</nav>

<section class="hero">
  <p class="hero-kicker">the bean cart</p>
  <h1 class="hero-title">We'd love to provide you with<br>a coffee experience that excites and delights.</h1>
  <div class="hero-button">See all our services</div>
  <div class="hero-dots"><span class="on"></span><span></span><span></span><span></span></div>
</section>

<h2 class="section-title difference-title">Why we are different?</h2>
<div class="points">
  <div class="point" style="left:97px">
    <svg width="40" height="40" viewBox="0 0 40 40">
      <path d="M20 4C10 4 3 11 3 20s7 16 15 16c3 0 4-2 3-4s0-4 3-4h4c6 0 9-4 9-9C37 11 30 4 20 4z" fill="none" stroke="var(--orange)" stroke-width="2.2"/>
      <circle cx="12" cy="17" r="2.5" fill="var(--orange)"/><circle cx="18" cy="11" r="2.5" fill="var(--orange)"/><circle cx="27" cy="12" r="2.5" fill="var(--orange)"/>
      <path d="M14 30L33 9" stroke="var(--orange)" stroke-width="3" stroke-linecap="round"/>
    </svg>
    <h3>We cater to your theme</h3>
    <p>We can provide a cart that blends seamlessly into your decor or theme. Whether it's a woodern, rustic or bright red, we have a cart and the coffee machines to suit every occasion</p>
  </div>
  <div class="point" style="left:365px">
    <svg width="40" height="40" viewBox="0 0 40 40">
      <circle cx="11" cy="7" r="4" fill="var(--orange)"/><circle cx="29" cy="7" r="4" fill="var(--orange)"/>
      <rect x="6" y="13" width="10" height="14" rx="2" fill="var(--orange)"/><rect x="24" y="13" width="10" height="14" rx="2" fill="var(--orange)"/>
      <rect x="7" y="27" width="3.5" height="11" fill="var(--orange)"/><rect x="11.5" y="27" width="3.5" height="11" fill="var(--orange)"/>
      <rect x="25" y="27" width="3.5" height="11" fill="var(--orange)"/><rect x="29.5" y="27" width="3.5" height="11" fill="var(--orange)"/>
      <rect x="16" y="17" width="8" height="3" fill="var(--orange)"/>
    </svg>
    <h3>We Go the extra mile</h3>
    <p>We love what we do and provide above and beyond service and hospitality.</p>
  </div>
  <div class="point" style="left:633px">
    <svg width="46" height="40" viewBox="0 0 46 40">
      <path d="M2 16l16-7v18L2 20z" fill="var(--orange)"/>
      <circle cx="30" cy="14" r="6" fill="var(--orange)"/>
      <path d="M20 36c0-8 4-13 10-13s10 5 10 13z" fill="var(--orange)"/>
    </svg>
    <h3>We listen to your needs</h3>
    <p>No two carts are the same as we understand that your event, theme or occasion are unique and special. We'd love to provide you with a coffee experience that excites and delights.</p>
  </div>
</div>

<div class="rule"></div>

<h2 class="section-title carts-title">Our carts at events</h2>
<div class="gallery">
  <div class="photo tall" role="img" aria-label="Outdoor coffee cart with a barista and a coffee sign at an event"></div>
  <div class="photo p1" role="img" aria-label="Rustic timber coffee cart at an indoor event"></div>
  <div class="photo p2" role="img" aria-label="Coffee machine and stacked takeaway cups on a cart"></div>
  <div class="photo p3" role="img" aria-label="Rustic timber coffee cart at an indoor event"></div>
  <div class="photo p4" role="img" aria-label="Espresso machine on a cart beneath a garden pergola"></div>
  <div class="photo p5" role="img" aria-label="Barista working at a cart inside a venue"></div>
  <div class="photo p6" role="img" aria-label="Espresso machine on a cart beneath a garden pergola"></div>
</div>

</body>
</html>
```